Property Consultancy require stationary

Property Consultancy K7 Group Ltd, slogan is Places Value Connections. Require letterhead, business card and Outlook email signature utilising existing logo design.

Property

```html
<!DOCTYPE html>
<html lang="en">
<head>
<meta charset="utf-8">
<title>K7 Group Ltd — Stationery</title>
<link rel="stylesheet" href="https://fonts.googleapis.com/css2?family=Source+Sans+3:ital,wght@0,400;0,600;1,600&family=Roboto+Condensed:wght@700&display=swap">
<style>
  :root {
    --backdrop: #222222;
    --paper: #ffffff;
    --brand-red: #e2292b;
    --brand-grey: #8a8a8a;
    --charcoal: #404040;
    --text-dark: #4a4a4a;
    --text-mid: #777777;
    --tint-red: #fdeced;
    --tint-grey: #f3f3f3;
  }
  * { margin: 0; padding: 0; box-sizing: border-box; }
  html, body {
    width: 1200px; height: 1000px; overflow: hidden;
    background: var(--backdrop);
    font-family: "Source Sans 3", sans-serif;
  }
  .canvas { position: relative; width: 1200px; height: 1000px; }

  /* Letterhead */
  .letterhead {
    position: absolute; left: 77px; top: 48px; width: 690px; height: 895px;
    background: var(--paper); overflow: hidden;
  }
  .letterhead__top { position: absolute; left: 0; top: 0; width: 100%; height: 14px; background: var(--charcoal); }
  .letterhead__top-rule { position: absolute; left: 0; top: 14px; width: 100%; height: 4px; background: var(--brand-red); }
  .letterhead__wash { position: absolute; left: 306px; top: 609px; width: 384px; height: 213px; background: var(--tint-red); }
  .letterhead__wash--grey { left: 421px; top: 456px; width: 269px; height: 120px; background: var(--tint-grey); }
  .letterhead__foot-rule { position: absolute; left: 0; top: 822px; width: 100%; height: 7px; background: var(--brand-red); }
  .letterhead__foot {
    position: absolute; left: 0; top: 829px; width: 100%; height: 66px;
    background: var(--charcoal);
    padding: 7px 10px 0 0; text-align: right;
    font-family: "Roboto Condensed", sans-serif; font-weight: 700;
    font-size: 9px; line-height: 12.5px; color: #ffffff;
  }
  .letterhead__foot .foot-name { font-size: 10px; }

  /* Brand lockup */
  .lockup { position: absolute; text-align: center; }
  .lockup__row { display: flex; align-items: center; justify-content: center; gap: 8px; }
  .lockup__square { width: 16px; height: 16px; background: var(--brand-red); }
  .lockup__name {
    font-weight: 600; color: var(--text-dark); letter-spacing: 1px; line-height: 1;
  }
  .lockup__slogan {
    color: var(--brand-grey); text-transform: uppercase; letter-spacing: 1px; margin-top: 4px;
  }
  .letterhead .lockup { left: 0; width: 100%; top: 88px; }
  .letterhead .lockup__name { font-size: 28px; }
  .letterhead .lockup__slogan { font-size: 7.5px; }

  /* Business cards */
  .card {
    position: absolute; width: 440px; height: 263px; background: var(--paper);
    overflow: hidden; box-shadow: 0 4px 10px rgba(0,0,0,0.5);
  }
  .card--front { left: 642px; top: 221px; }
  .card--back { left: 643px; top: 527px; height: 262px; }
  .card__band { position: absolute; left: 0; }
  .card--front .card__band { top: 91px; width: 350px; height: 54px; background: var(--brand-red); }
  .card--back .card__band { top: 77px; width: 230px; height: 56px; background: var(--brand-grey); }

  .card--front .lockup { right: 30px; top: 212px; text-align: right; }
  .card--front .lockup__row { justify-content: flex-end; }
  .card--front .lockup__name { font-size: 26px; }
  .card--front .lockup__slogan { font-size: 7.5px; margin-top: 3px; }

  .card--back .lockup { left: 44px; top: 203px; }
  .card--back .lockup__square { width: 11px; height: 11px; }
  .card--back .lockup__name { font-size: 17px; }
  .card--back .lockup__slogan { font-size: 5.5px; margin-top: 3px; }

  .contact { position: absolute; right: 58px; top: 100px; text-align: right; }
  .contact__name { font-size: 19px; color: var(--text-dark); line-height: 24px; }
  .contact__role { font-size: 15px; font-weight: 600; font-style: italic; color: var(--brand-red); line-height: 17px; }
  .contact__line { font-size: 13.5px; color: var(--text-mid); line-height: 15px; }
  .contact__line--first { margin-top: 10px; }
</style>
</head>
<body>
<main class="canvas">
  <section class="letterhead" aria-label="Letterhead">
    <div class="letterhead__top"></div>
    <div class="letterhead__top-rule"></div>
    <div class="lockup">
      <div class="lockup__row"><span class="lockup__square"></span><span class="lockup__name">K7 GROUP</span></div>
      <div class="lockup__slogan">Places Value Connections</div>
    </div>
    <div class="letterhead__wash letterhead__wash--grey"></div>
    <div class="letterhead__wash"></div>
    <div class="letterhead__foot-rule"></div>
    <footer class="letterhead__foot">
      <div class="foot-name">K7 Group</div>
      <div>Telephone: 123 555 0190</div>
      <div>Email: info@k7group.com</div>
      <div>Website: www.k7group.com</div>
    </footer>
  </section>

  <section class="card card--front" aria-label="Business card front">
    <div class="card__band"></div>
    <div class="lockup">
      <div class="lockup__row"><span class="lockup__square"></span><span class="lockup__name">K7 GROUP</span></div>
      <div class="lockup__slogan">Places Value Connections</div>
    </div>
  </section>

  <section class="card card--back" aria-label="Business card back">
    <div class="card__band"></div>
    <div class="contact">
      <div class="contact__name">Daniel Reyes</div>
      <div class="contact__role">President</div>
      <div class="contact__line contact__line--first">512 555 0147</div>
      <div class="contact__line">d.reyes@k7group.com</div>
    </div>
    <div class="lockup">
      <div class="lockup__row"><span class="lockup__square"></span><span class="lockup__name">K7 GROUP</span></div>
      <div class="lockup__slogan">Places Value Connections</div>
    </div>
  </section>
</main>
</body>
</html>
```